Cognitive therapist.

I am a therapist and my main work is with clients who have depression and anxiety disorders.

I need something reasonably plain. Cognitive therapy is a very pragmatic approach to dealing with problems, so it isn't new agey (no offence to new age therapies at all)

Hi everyone, I am currently looking at a particular design that I will most likely go with. Cheers, Mel

Mel Tarrow
Cognitive Therapist
BA, PG Dip Mental Health,
PG Dip Cog Beh Therapy
MKLPT

The Larchmont Rooms,
Level One
57 Quillon Parade
Cnr Fenwick St & Quillon Parade
P O Box 38 215
WELLINGTON 6281

Phone: 027 534 2870 Email: mtarrow@vexmail.co.nz

www.meltarrow.co.nz

• No illustration, or colour. not old style fonts.

```html
<!DOCTYPE html>
<html lang="en">
<head>
<meta charset="utf-8">
<title>Mel Tarrow · Cognitive Therapist</title>
<link rel="stylesheet" href="https://fonts.googleapis.com/css2?family=Bodoni+Moda:ital,opsz,wght@0,6..96,400;1,6..96,400&family=Mulish:ital,wght@0,400;1,400&display=swap">
<style>
  :root {
    --paper: #ffffff;
    --ink: #111111;
    --rule: #1a1a1a;
  }
  * { margin: 0; padding: 0; box-sizing: border-box; }
  html, body {
    width: 1200px;
    height: 740px;
    overflow: hidden;
    background: var(--paper);
  }
  .card {
    position: relative;
    width: 1200px;
    height: 740px;
    background: var(--paper);
    color: var(--ink);
  }
  .card__name {
    position: absolute;
    top: 72px;
    left: 0;
    width: 100%;
    text-align: center;
    font-family: "Bodoni Moda", serif;
    font-style: italic;
    font-size: 56px;
    line-height: 1;
    letter-spacing: 1px;
    font-weight: 400;
  }
  .card__rule {
    position: absolute;
    top: 153px;
    left: 219px;
    width: 776px;
    height: 8px;
  }
  .card__role {
    position: absolute;
    top: 180px;
    left: 0;
    width: 100%;
    text-align: center;
    font-family: "Bodoni Moda", serif;
    font-size: 37px;
    line-height: 1;
    letter-spacing: 2px;
    text-transform: uppercase;
    font-weight: 400;
  }
  .card__credentials {
    position: absolute;
    top: 280px;
    left: 0;
    width: 100%;
    text-align: center;
    font-family: "Mulish", sans-serif;
    font-style: italic;
    font-size: 31px;
    line-height: 49px;
    letter-spacing: 2.6px;
  }
  .card__address,
  .card__contact {
    position: absolute;
    font-family: "Mulish", sans-serif;
    font-size: 28px;
    line-height: 40.5px;
    font-style: normal;
  }
  .card__address {
    top: 492px;
    left: 135px;
  }
  .card__contact {
    top: 532px;
    right: 125px;
    text-align: right;
  }
</style>
</head>
<body>
  <main class="card">
    <h1 class="card__name">· MEL TARROW ·</h1>
    <svg class="card__rule" viewBox="0 0 776 8" aria-hidden="true">
      <polygon points="0,4 388,2.6 776,4 388,5.4" fill="var(--rule)"/>
    </svg>
    <p class="card__role">Cognitive Therapist</p>
    <p class="card__credentials">
      BA, Pg Dip Mental Health,<br>
      Pg Dip Cognitive Behavioural,<br>
      Therapy with Distinction, MKLPT
    </p>
    <address class="card__address">
      The Larchmont Rooms<br>
      57 Quillon Parade<br>
      Corner Fenwick Street &amp; Quillon Parade<br>
      Wellington 6281
    </address>
    <address class="card__contact">
      Phone: 027 534 2870<br>
      Email: mtarrow@vexmail.co.nz<br>
      www.meltarrow.co.nz
    </address>
  </main>
</body>
</html>
```